Business Card Design

TAX PREPARATION CO.
INCOME & SALES TAXES
ELECTRONIC FILING
ESTABLISHED IN 1993
Looking for a design with a lady at a table with a pen over a 1040 form looking puzzled and a bubble with wording I'm in over my head.

Industry/Entity Type

Business

Contact Information for Business Card

LEDGERLY PLUS INC

```html
<!DOCTYPE html>
<html lang="en">
<head>
<meta charset="utf-8">
<title>Ledgerly Plus Inc — Business Card</title>
<link rel="stylesheet" href="https://fonts.googleapis.com/css2?family=Arimo:wght@700&family=Cormorant+Garamond:wght@500&family=Kurale&family=Roboto:wght@400;700&display=swap">
<style>
  :root {
    --backdrop: #7b7c7e;
    --card: #ffffff;
    --band-red: #c5332d;
    --band-red-dark: #9e1f1b;
    --band-edge: #2a2a2a;
    --title-silver: #e3e7f2;
    --ink: #2b2b2b;
    --accent-red: #b8231e;
    --divider: #3a3a3a;
    --art-hair: #b9773e;
    --art-shirt: #c9dcf0;
    --art-desk: #ece9ee;
  }
  * { box-sizing: border-box; margin: 0; padding: 0; }
  html, body { width: 1200px; height: 900px; overflow: hidden; }
  body { background: var(--backdrop); position: relative; }

  .card {
    position: absolute; left: 100px; top: 180px;
    width: 1000px; height: 540px;
    background: var(--card);
    border-radius: 34px;
    overflow: hidden;
  }

  .brand-band {
    position: absolute; left: 0; right: 0; top: 160px; height: 146px;
    background: linear-gradient(180deg, var(--band-red) 0%, var(--band-red-dark) 100%);
    border-top: 4px solid var(--band-edge);
    border-bottom: 4px solid var(--band-edge);
  }

  .illustration {
    position: absolute; left: 20px; top: 40px;
    width: 300px; height: 440px;
    border-radius: 14px;
    background: linear-gradient(180deg, var(--art-hair) 0%, #d9a27a 30%, var(--art-shirt) 58%, var(--art-desk) 100%);
  }

  .speech-bubble {
    position: absolute; left: 300px; top: 40px;
    width: 170px; height: 150px;
  }
  .speech-bubble svg { position: absolute; inset: 0; }
  .speech-bubble p {
    position: relative;
    padding-top: 18px;
    font: 700 25px/1.3 "Roboto", sans-serif;
    color: #111;
    text-align: center;
  }

  .company-name {
    position: absolute; left: 335px; right: 20px; top: 196px;
    text-align: center;
    white-space: nowrap;
    font: 700 54px/1 "Arimo", sans-serif;
    color: var(--title-silver);
  }
  .established {
    position: absolute; left: 335px; right: 20px; top: 264px;
    text-align: center;
    white-space: nowrap;
    font: 400 17px/1 "Roboto", sans-serif;
    letter-spacing: 2.5px;
    color: var(--ink);
  }

  .person {
    position: absolute; right: 492px; top: 408px;
    text-align: right;
    white-space: nowrap;
  }
  .person-name {
    font: 500 32px/1 "Cormorant Garamond", serif;
    color: var(--accent-red);
  }
  .person-role {
    margin-top: 8px;
    font: 400 18px/1 "Kurale", serif;
    color: var(--ink);
  }

  .divider {
    position: absolute; left: 518px; top: 330px;
    width: 2px; height: 170px;
    background: var(--divider);
  }

  .contact-list {
    position: absolute; left: 530px; top: 330px;
    list-style: none;
  }
  .contact-list li {
    display: flex; align-items: center; gap: 6px;
    height: 32px;
    white-space: nowrap;
    font: 400 20px/1 "Kurale", serif;
    color: var(--ink);
  }
  .contact-list svg { width: 22px; height: 22px; flex: none; fill: var(--accent-red); }
</style>
</head>
<body>
  <section class="card">
    <div class="brand-band"></div>

    <div class="illustration" role="img" aria-label="Cartoon illustration of a smiling woman in a light blue blouse seated at a desk with a pen over a tax form"></div>

    <div class="speech-bubble">
      <svg viewBox="0 0 170 150" aria-hidden="true">
        <path d="M22 6 H150 Q164 6 164 20 V112 Q164 126 150 126 H40 L10 146 L22 124 Q8 120 8 106 V20 Q8 6 22 6 Z"
              fill="#fff" stroke="var(--accent-red)" stroke-width="5"/>
      </svg>
      <p>I'm in<br>over my<br>head.</p>
    </div>

    <h1 class="company-name">LEDGERLY PLUS INC</h1>
    <p class="established">ESTABLISHED IN 1993</p>

    <div class="person">
      <p class="person-name">Maren Holloway</p>
      <p class="person-role">manager</p>
    </div>

    <div class="divider"></div>

    <ul class="contact-list">
      <li>
        <svg viewBox="0 0 24 24" aria-hidden="true"><path d="M6.6 10.8a15.1 15.1 0 0 0 6.6 6.6l2.2-2.2c.3-.3.7-.4 1-.2 1.1.4 2.3.6 3.6.6.6 0 1 .4 1 1V20c0 .6-.4 1-1 1A17 17 0 0 1 3 4c0-.6.4-1 1-1h3.5c.6 0 1 .4 1 1 0 1.3.2 2.5.6 3.6.1.3 0 .7-.2 1z"/></svg>
        (555) 014-2231
      </li>
      <li>
        <svg viewBox="0 0 24 24" aria-hidden="true"><path d="M7 3h10v5H7zM4 9h16a2 2 0 0 1 2 2v6h-4v4H6v-4H2v-6a2 2 0 0 1 2-2zm4 7v3h8v-3z"/></svg>
        (555) 014-7780
      </li>
      <li>
        <svg viewBox="0 0 24 24" aria-hidden="true"><path d="M3 5h18a1 1 0 0 1 1 1v12a1 1 0 0 1-1 1H3a1 1 0 0 1-1-1V6a1 1 0 0 1 1-1zm1 2.3V17h16V7.3l-8 5.2z"/></svg>
        info@ledgerlyplus.com
      </li>
      <li>
        <svg viewBox="0 0 24 24" aria-hidden="true"><path d="M12 2a10 10 0 1 0 0 20 10 10 0 0 0 0-20zm6.9 9h-3a15 15 0 0 0-1.3-6 8 8 0 0 1 4.3 6zM12 4.1c.9 1.3 1.7 3.6 1.9 6.9h-3.8c.2-3.3 1-5.6 1.9-6.9zM9.4 5a15 15 0 0 0-1.3 6h-3a8 8 0 0 1 4.3-6zM5.1 13h3a15 15 0 0 0 1.3 6 8 8 0 0 1-4.3-6zm6.9 6.9c-.9-1.3-1.7-3.6-1.9-6.9h3.8c-.2 3.3-1 5.6-1.9 6.9zm2.6-.9a15 15 0 0 0 1.3-6h3a8 8 0 0 1-4.3 6z"/></svg>
        www.ledgerlyplus.com
      </li>
      <li>
        <svg viewBox="0 0 24 24" aria-hidden="true"><path d="M12 3 2 12h3v9h5v-6h4v6h5v-9h3z"/></svg>
        4180 Harbor Road, Suite B, Fairhaven,
      </li>
    </ul>
  </section>
</body>
</html>
```